Mobile Friendly Lead Generation Landing Page

We are a web marketing company that specialized in web lead generation. Recently we have started buying media from mobile devices and we need a mobile interface(landing page) where we can collect user data in an effective manner.

Our current mobile landing page is:
http://www.tuitionscout.example.com/lp13d/index.aspx?a=true&source=581406
Through this you can see what the steps/questions users need to answer to get matched to a school. We need the design for the whole process.

We are pretty open for design ideas and our goal is to make this mobile optimized landing page have the look and feel of an app...but not an app.
There are several questions in the process but we are open to changing the way they are presented. As in, you can have one question at a time or a few.
The goal is to make this EXTREMELY EASY for users to interact with.

One example that we have liked is:
http://lessonhub.example/schools/47215-page1.lhub (please note that this opens only on mobile devices)

Some of these screenshots are attached.

Our web form looks like this:
http://www.tuitionscout.example.com/lp88/index.aspx?a=true

```html
<!DOCTYPE html>
<html lang="en">
<head>
<meta charset="utf-8">
<title>TuitionScout – Field of Interest</title>
<link rel="stylesheet" href="https://fonts.googleapis.com/css2?family=Arimo:wght@400;700&display=swap">
<style>
  :root {
    --page-bg: #eeeeee;
    --screen-bg: #ffffff;
    --ink: #1a1a1a;
    --logo-ink: #4a4a48;
    --lime: #a8cc3c;
    --lime-light: #c9e27a;
    --lime-deep: #8db52a;
    --btn-top: #34b9e6;
    --btn-bottom: #0d93c9;
    --btn-edge: #0a7fb0;
    --btn-text: #ffffff;
    --list-bg: #f3f4f4;
  }
  * { box-sizing: border-box; margin: 0; padding: 0; }
  html, body {
    width: 1200px; height: 800px; overflow: hidden;
    background: radial-gradient(ellipse at center, #fafafa 0%, var(--page-bg) 75%);
    font-family: "Arimo", Arial, sans-serif;
    color: var(--ink);
  }
  .canvas {
    width: 1200px; height: 800px;
    display: flex; align-items: center; justify-content: center;
  }
  .landing {
    width: 430px; height: 706px;
    background: var(--screen-bg);
    display: flex; flex-direction: column;
    box-shadow: 0 2px 14px rgba(0,0,0,0.12);
    overflow: hidden;
  }
  .brand-bar {
    height: 104px;
    display: flex; align-items: center; justify-content: center; gap: 12px;
  }
  .brand-mark {
    width: 30px; height: 30px; border-radius: 50%;
    background: var(--lime);
  }
  .brand-name {
    font-size: 44px; font-weight: 700; letter-spacing: -1px;
    color: var(--logo-ink);
  }
  .form-ribbon {
    height: 23px; position: relative;
    background: linear-gradient(90deg, var(--lime-deep) 0%, var(--lime) 45%, var(--lime-light) 72%, rgba(201,226,122,0) 100%);
    display: flex; align-items: center; justify-content: center;
  }
  .form-ribbon span {
    color: #fff; font-size: 14px; text-shadow: 0 1px 1px rgba(0,0,0,0.2);
  }
  .question {
    flex: 1;
    background: linear-gradient(180deg, #ffffff 0%, var(--list-bg) 12%, #ffffff 30%);
    padding: 22px 35px 0;
  }
  .question-label {
    font-size: 14px; margin: 0 0 18px -4px;
  }
  .field-list { list-style: none; }
  .field-option {
    height: 51px; margin-bottom: 13px;
    border-radius: 4px;
    background: linear-gradient(180deg, var(--btn-top) 0%, var(--btn-top) 48%, var(--btn-bottom) 52%, var(--btn-bottom) 100%);
    border-bottom: 2px solid var(--btn-edge);
    display: flex; align-items: center; justify-content: space-between;
    padding: 0 18px 0 22px;
    color: var(--btn-text); font-size: 17px;
    box-shadow: 0 1px 2px rgba(0,0,0,0.2);
  }
  .field-option svg { width: 14px; height: 18px; }
  .field-option.is-first { background: linear-gradient(180deg, var(--btn-top) 0%, var(--btn-top) 48%, var(--btn-bottom) 52%, var(--btn-bottom) 88%, #0b86bb 100%); }
  .legal-footer {
    height: 58px;
    background: var(--lime);
    padding: 8px 40px 0;
    text-align: center;
  }
  .legal-footer p {
    font-size: 7px; line-height: 1.35; text-align: left; color: #222;
  }
  .powered {
    margin-top: 5px; font-size: 6px; color: #222;
    display: flex; flex-direction: column; align-items: center; gap: 2px;
  }
  .partner-badge { width: 22px; height: 9px; background: #2b8fc7; }
</style>
</head>
<body>
<div class="canvas">
  <main class="landing">
    <header class="brand-bar">
      <span class="brand-mark"></span>
      <span class="brand-name">TuitionScout</span>
    </header>
    <div class="form-ribbon"><span>Fill Out Our 2 Minutes Form</span></div>
    <section class="question">
      <p class="question-label">Please select your field of interest:</p>
      <ul class="field-list">
        <li class="field-option is-first">Business<svg viewBox="0 0 14 18"><path d="M4 3l6 6-6 6" fill="none" stroke="#fff" stroke-width="2.5"/></svg></li>
        <li class="field-option">Criminal Justice<svg viewBox="0 0 14 18"><path d="M4 3l6 6-6 6" fill="none" stroke="#fff" stroke-width="2.5"/></svg></li>
        <li class="field-option">Education &amp; Teaching<svg viewBox="0 0 14 18"><path d="M4 3l6 6-6 6" fill="none" stroke="#fff" stroke-width="2.5"/></svg></li>
        <li class="field-option">Health Care<svg viewBox="0 0 14 18"><path d="M4 3l6 6-6 6" fill="none" stroke="#fff" stroke-width="2.5"/></svg></li>
        <li class="field-option">Human Services<svg viewBox="0 0 14 18"><path d="M4 3l6 6-6 6" fill="none" stroke="#fff" stroke-width="2.5"/></svg></li>
        <li class="field-option">Psychology<svg viewBox="0 0 14 18"><path d="M4 3l6 6-6 6" fill="none" stroke="#fff" stroke-width="2.5"/></svg></li>
        <li class="field-option">Social Services<svg viewBox="0 0 14 18"><path d="M4 3l6 6-6 6" fill="none" stroke="#fff" stroke-width="2.5"/></svg></li>
      </ul>
    </section>
    <footer class="legal-footer">
      <p>Financial aid may be offered to those who qualify. To learn if you qualify for aid of any kind, please speak with an adviser at one of our partner schools.</p>
      <div class="powered"><span>Powered by</span><span class="partner-badge"></span></div>
    </footer>
  </main>
</div>
</body>
</html>
```